Corvath Staffing Solutions - Magazine Ad

Local magazine ad for Corvath Staffing Solutions.
We are targeting local businesses, namely hospitality clients in the local Laguna Beach, CA area. This is an upscale, rather fancy, area so the target audience will be of a more professional sense. We want this advertisement to stand out from the rest. Feel free to use beach and other Laguna Beach, CA pics.
We want to provide the following contact info, clearly visible to direct traffic.
Contact info:
Dana Whitcombe
dwhitcombe@Brisdel.example
949-382-0465
Should include the text:
"Servicing:
- Professional
- Clerical
- Hospitality
- FInancial
- Highly Skilled Industrial"
Please include: www.Brisdel.example
This will be a full page ad.

```html
<!DOCTYPE html>
<html lang="en">
<head>
<meta charset="utf-8">
<title>Corvath Staffing Solutions – Magazine Ad</title>
<link rel="stylesheet" href="https://fonts.googleapis.com/css2?family=Mulish:wght@700&family=Questrial&display=swap">
<style>
  :root {
    --paper: #ffffff;
    --ink: #2b2b2e;
    --night: #0b0b0f;
    --slate: #2b3237;
    --slate-deep: #1c2328;
    --brand-blue: #2f7fc8;
    --brand-blue-soft: rgba(60, 140, 215, 0.55);
    --accent: #f4a630;
    --light: #ffffff;
  }
  html, body {
    margin: 0;
    padding: 0;
    overflow: hidden;
    background: var(--paper);
  }
  .ad {
    position: relative;
    width: 927px;
    height: 1200px;
    overflow: hidden;
    background: var(--night);
    font-family: "Questrial", "Century Gothic", sans-serif;
  }
  .ad__photo {
    position: absolute;
    left: 0; top: 0;
    width: 927px; height: 622px;
    background:
      radial-gradient(ellipse at 48% 35%, #e9eef3 0%, #cdd6de 45%, transparent 70%),
      linear-gradient(90deg, #3a4655 0%, #c9d2db 30%, #eef2f6 50%, #aab7c4 75%, #3d4a5a 100%);
  }
  .ad__shapes {
    position: absolute;
    left: 0; top: 0;
    width: 927px; height: 1200px;
  }
  .pitch {
    position: absolute;
    left: 24px;
    top: 658px;
    width: 400px;
    color: var(--ink);
  }
  .pitch__headline {
    margin: 0;
    font-family: "Mulish", "Century Gothic", sans-serif;
    font-weight: 700;
    font-size: 21px;
    line-height: 41.5px;
  }
  .pitch__body {
    margin: 28px 0 0;
    font-size: 19.5px;
    line-height: 41.5px;
  }
  .brand {
    position: absolute;
    left: 24px;
    top: 1110px;
    display: flex;
    align-items: center;
    gap: 12px;
    color: var(--brand-blue);
    font-size: 30px;
    letter-spacing: 3px;
  }
  .brand__square {
    width: 26px;
    height: 26px;
    background: var(--brand-blue);
  }
  .services {
    position: absolute;
    right: 27px;
    top: 688px;
    text-align: right;
    color: var(--light);
    margin: 0;
    padding: 0;
    list-style: none;
  }
  .services__title {
    color: var(--accent);
    font-family: "Mulish", "Century Gothic", sans-serif;
    font-weight: 700;
    font-size: 27px;
    line-height: 40px;
    margin: 0 0 6px;
  }
  .services__item {
    font-size: 24px;
    line-height: 42.5px;
  }
  .services__item--stack { line-height: 32px; padding-top: 5px; }
  .contact {
    position: absolute;
    right: 27px;
    top: 1052px;
    text-align: right;
    color: var(--accent);
    font-size: 19.5px;
    line-height: 43px;
    font-style: normal;
  }
  .contact a { color: inherit; text-decoration: none; }
  .web {
    position: absolute;
    left: 403px;
    top: 1138px;
    color: var(--light);
    font-size: 19.5px;
    text-decoration: none;
  }
</style>
</head>
<body>
<main class="ad">
  <div class="ad__photo" role="img" aria-label="Photo of a smiling businesswoman holding a pen in front of a team of colleagues in business suits, in a bright office"></div>

  <svg class="ad__shapes" viewBox="0 0 850 1100" preserveAspectRatio="none" aria-hidden="true">
    <!-- diagonal blue bands over the photo -->
    <polygon points="850,0 850,70 390,570 325,570" fill="var(--brand-blue-soft)"/>
    <polygon points="850,210 850,330 610,570 480,570" fill="rgba(35,95,160,0.6)"/>
    <polygon points="760,570 850,480 850,570" fill="rgba(30,70,120,0.7)"/>
    <!-- lower panel -->
    <rect x="0" y="570" width="850" height="530" fill="var(--night)"/>
    <polygon points="320,570 720,570 520,770 420,670" fill="var(--slate)"/>
    <polygon points="320,570 420,570 470,620 420,670" fill="var(--slate-deep)"/>
    <polygon points="0,570 320,570 528,776 208,1100 0,1100" fill="var(--paper)"/>
  </svg>

  <section class="pitch">
    <h1 class="pitch__headline">Staffing solutions that work.<br>Nationwide full-time, part-time,<br>and temporary positions.</h1>
    <p class="pitch__body">Corvath Staffing Solutions takes an innovative approach to staffing in order to provide you with the most comprehensive solutions possible.</p>
  </section>

  <div class="brand"><span class="brand__square"></span><span class="brand__name">Brisdel</span></div>

  <ul class="services">
    <li class="services__title">Servicing</li>
    <li class="services__item">Professional</li>
    <li class="services__item">Clerical</li>
    <li class="services__item">Hospitality</li>
    <li class="services__item">FInancial</li>
    <li class="services__item services__item--stack">Highly Skilled<br>Industrial</li>
  </ul>

  <address class="contact">
    Dana Whitcombe<br>
    <a href="mailto:dwhitcombe@Brisdel.example">dwhitcombe@Brisdel.example</a><br>
    949-382-0465
  </address>

  <a class="web" href="#">www.Brisdel.example</a>
</main>
</body>
</html>
```